Business Card for Managing Partner Investment Fund

To create a business card template for an investment fund manager. Business card should be more professional in nature, not too colorful, more upscale, and created using the attached logos and fund name files. I would prefer a black or gray color scheme, but am open to the use of color as well. I would prefer a double sided business card, but open to single sided business card designs as well. The business card should include: name, title, and contact information, as well as logo and company name. I would prefer a more stream-lined, simple business card design.
Updates
Address: 4190 NE 38th Ter. Ocala, FL 34470
Email: talvin47@quorimail.net
Phone: 561-347-9162
Title: managing partner
Name: Dorian Velsky
Fund Name: Ambergate Capital
Logos can be found in files attached to the brief
Target Market(s)
potential investors, other fund managers
Industry/Entity Type
Finance
Contact Information for Business Card
Name on card: Dorian Velsky
Title: Managing Partner
Colors
Designer to choose colors to be used in the design.
Requirements
Must have
- Phone number
- email address
- physical address
- title
- name
- logo
- Fund name
Nice to have
- simple layout
Should not have
- too many colors, busy fonts,

```html
<!DOCTYPE html>
<html lang="en">
<head>
<meta charset="utf-8">
<title>Ambergate Capital — Business Card</title>
<link rel="stylesheet" href="https://fonts.googleapis.com/css2?family=Cinzel:wght@400;600&family=Montserrat:wght@300;400&display=swap">
<style>
  :root {
    --backdrop: #2b2b2b;
    --card: #050505;
    --white: #f4f4f4;
    --grey: #8c8c8c;
    --grey-dark: #6e6e6e;
  }
  * { margin: 0; padding: 0; box-sizing: border-box; }
  html, body {
    width: 1200px;
    height: 900px;
    overflow: hidden;
    background: var(--backdrop);
  }
  .sheet {
    width: 1200px;
    height: 900px;
    display: flex;
    flex-direction: column;
    align-items: center;
    justify-content: center;
    gap: 40px;
  }
  .card {
    position: relative;
    width: 700px;
    height: 400px;
    background: var(--card);
    overflow: hidden;
  }

  /* Front side */
  .card-front {
    display: flex;
    align-items: center;
    justify-content: center;
  }
  .front-name {
    font-family: 'Cinzel', serif;
    font-weight: 600;
    font-size: 44px;
    letter-spacing: 3px;
    color: var(--white);
    text-transform: uppercase;
  }

  /* Back side */
  .back-name {
    position: absolute;
    top: 58px;
    right: 56px;
    font-family: 'Cinzel', serif;
    font-weight: 600;
    font-size: 24px;
    letter-spacing: 1.5px;
    color: var(--grey);
    text-transform: uppercase;
  }
  .holder {
    position: absolute;
    top: 160px;
    right: 70px;
    text-align: right;
    font-family: 'Cinzel', serif;
    font-weight: 400;
    font-size: 19px;
    letter-spacing: 1.5px;
    color: var(--grey-dark);
    text-transform: uppercase;
  }
  .holder-rule {
    position: absolute;
    top: 190px;
    left: 320px;
    right: 0;
    height: 2px;
    background: var(--white);
  }
  .title {
    position: absolute;
    top: 198px;
    right: 70px;
    font-family: 'Montserrat', sans-serif;
    font-weight: 400;
    font-size: 15px;
    color: var(--white);
  }
  .contacts {
    position: absolute;
    top: 226px;
    right: 36px;
    list-style: none;
    font-family: 'Montserrat', sans-serif;
    font-weight: 300;
    font-size: 14px;
    color: var(--grey);
  }
  .contacts li {
    display: flex;
    justify-content: flex-end;
    align-items: center;
    gap: 16px;
    height: 24px;
  }
  .contacts .icon {
    width: 14px;
    height: 14px;
    fill: var(--white);
    flex: none;
  }
  .contacts .no-icon { padding-right: 30px; }
  .base-rule {
    position: absolute;
    left: 0;
    top: 346px;
    width: 420px;
    height: 2px;
    background: var(--white);
  }
</style>
</head>
<body>
<main class="sheet">
  <section class="card card-front" aria-label="Card front">
    <h1 class="front-name">Ambergate Capital</h1>
  </section>

  <section class="card card-back" aria-label="Card back">
    <p class="back-name">Ambergate Capital</p>
    <p class="holder">Dorian Velsky</p>
    <div class="holder-rule"></div>
    <p class="title">Managing Partner</p>
    <ul class="contacts">
      <li>561-347-9162
        <svg class="icon" viewBox="0 0 24 24" aria-hidden="true"><path d="M6.6 10.8a15.1 15.1 0 0 0 6.6 6.6l2.2-2.2a1 1 0 0 1 1-.25 11.4 11.4 0 0 0 3.6.57 1 1 0 0 1 1 1V20a1 1 0 0 1-1 1A17 17 0 0 1 3 4a1 1 0 0 1 1-1h3.5a1 1 0 0 1 1 1c0 1.25.2 2.45.57 3.57a1 1 0 0 1-.25 1z"/></svg>
      </li>
      <li>talvin47@quorimail.net
        <svg class="icon" viewBox="0 0 24 24" aria-hidden="true"><path d="M2 5h20v14H2z" fill="none" stroke="#f4f4f4" stroke-width="2"/><path d="M2 5l10 8 10-8" fill="none" stroke="#f4f4f4" stroke-width="2"/></svg>
      </li>
      <li>4190 NE 38th Ter. Ocala, FL 34470
        <svg class="icon" viewBox="0 0 24 24" aria-hidden="true"><path d="M12 3l10 9h-3v9h-5v-6h-4v6H5v-9H2z"/></svg>
      </li>
    </ul>
    <div class="base-rule"></div>
  </section>
</main>
</body>
</html>
```